Letterhead Design Project

We store & repair empty shipping containers owned by the shipping lines.
We have just selected a logo design & now want a business card & letterhead to go with it. (Logo is attached - colours are yellow & dark grey)

ABN: 384 920 17263
ACN: 293 718 406
Address: 218-220 Pellgrove Rd, Marrowdale, 3047
Website: www.tarvelhub.com.au

You will need to make provision for a phone number, fax number & email (which we don't have yet.. so okay to just put in fake ones)

Target Market(s)

Shipping lines, freight forwarders

Industry/Entity Type

Shipping

Requirements
Must have
• Must include the logo attached
Must include our ABN, ACN address as per above

```html
<!DOCTYPE html>
<html lang="en">
<head>
<meta charset="utf-8">
<title>TarvelHub Business Card</title>
<link rel="stylesheet" href="https://fonts.googleapis.com/css2?family=Open+Sans:wght@400;600;700;800&display=swap">
<style>
  :root {
    --canvas: #f4ebe0;
    --yellow: #fdbd16;
    --slate: #3a4a54;
    --white: #ffffff;
  }
  html, body {
    margin: 0;
    padding: 0;
    overflow: hidden;
  }
  body {
    width: 1200px;
    height: 1000px;
    background: var(--canvas);
    position: relative;
    font-family: "Open Sans", Arial, sans-serif;
  }
  .card {
    position: absolute;
    top: 102px;
    width: 543px;
    height: 307px;
    overflow: hidden;
  }
  .card-front {
    left: 42px;
    background: var(--white);
    border-radius: 0 30px 0 30px;
  }
  .card-back {
    left: 617px;
    background: var(--yellow);
    border-radius: 30px 0 30px 0;
    color: var(--white);
    text-align: center;
  }
  .brand {
    display: flex;
    align-items: center;
    gap: 10px;
    font-weight: 800;
    letter-spacing: -0.5px;
    line-height: 1;
  }
  .brand-mark {
    display: block;
    flex: none;
  }
  .card-front .brand {
    position: absolute;
    left: 32px;
    top: 44px;
    font-size: 40px;
    color: var(--slate);
  }
  .card-front .brand-mark {
    width: 26px;
    height: 26px;
    background: var(--yellow);
  }
  .card-back .brand {
    position: absolute;
    left: 0;
    right: 0;
    top: 70px;
    justify-content: center;
    font-size: 54px;
    color: var(--white);
  }
  .card-back .brand-mark {
    width: 34px;
    height: 34px;
    background: var(--slate);
  }
  .holder {
    position: absolute;
    left: 33px;
    top: 120px;
  }
  .holder-name {
    font-size: 24px;
    color: var(--slate);
    line-height: 32px;
  }
  .holder-role {
    font-size: 20px;
    color: var(--yellow);
    line-height: 24px;
  }
  .contact-band {
    position: absolute;
    left: 0;
    right: 0;
    bottom: 0;
    height: 119px;
    background: var(--slate);
  }
  .contact-list {
    position: absolute;
    left: 33px;
    top: 22px;
    margin: 0;
    padding: 0;
    list-style: none;
    font-size: 16px;
    line-height: 20px;
    color: var(--white);
  }
  .company-details {
    position: absolute;
    left: 0;
    right: 0;
    top: 168px;
    font-size: 16px;
    line-height: 20px;
  }
  .company-details p {
    margin: 0;
  }
  .company-web {
    position: absolute;
    left: 0;
    right: 0;
    top: 240px;
    font-size: 24px;
    font-weight: 700;
    line-height: 32px;
  }
</style>
</head>
<body>
  <section class="card card-front" aria-label="Business card front">
    <div class="brand"><span class="brand-mark"></span>TarvelHub</div>
    <div class="holder">
      <div class="holder-name">Name Surname</div>
      <div class="holder-role">position</div>
    </div>
    <div class="contact-band">
      <ul class="contact-list">
        <li>t. 001.555.555.555</li>
        <li>f. 001.555.555.555</li>
        <li>e. office@tarvelhub.com.au</li>
      </ul>
    </div>
  </section>

  <section class="card card-back" aria-label="Business card back">
    <div class="brand"><span class="brand-mark"></span>TarvelHub</div>
    <div class="company-details">
      <p>ABN: 384 920 17263</p>
      <p>ACN: 293 718 406</p>
      <p>218-220 Pellgrove Rd, Marrowdale, 3047</p>
    </div>
    <div class="company-web">www.tarvelhub.com.au</div>
  </section>
</body>
</html>
```